We need to a website for a contact center that provides answering services by voice and chat.

A similar website in terms of design is the following site:
http://www.brindlecallhub.net/

The colors and look and feel should be different and creative but the structure should be similar to the above mentioned website.

Attached is the text file.

The design should communicate professionalism and friendly customer service oriented company. The visitor to the site must have a feel that "this company looks professional and they will take care of my client."

I am looking for design only, but if the designer will also do the coding, it will be an advantage.

Target Market(s)

Our target market are lawyers and doctors who require someone to answer their clients calls 24/7.

Industry/Entity Type

It Company

Requirements
Nice to have
• Since the company is based in Dubai, the website should reflect the Middle East people not pure European or pure Asians. A mixture of nationalities is fine to be visible in the pictures but it must include at least an arab or middle eastern person.
Should not have
• No old style, Times Roman font, do not include illustrations or cartoon graphics or pictures that are very common or widely used.

```html
<!DOCTYPE html>
<html lang="en">
<head>
<meta charset="utf-8">
<title>Cedar Voice – 24/7 Live Receptionist &amp; Answering Service</title>
<link rel="stylesheet" href="https://fonts.googleapis.com/css2?family=Roboto:wght@300;400;500;700;900&display=swap">
<style>
:root{
  --blue:#1b9ad6;
  --blue-dark:#0d6fae;
  --ink:#333;
  --body:#555;
  --muted:#999;
  --line:#ddd;
  --red:#d10a0a;
  --footer:#1b1b1b;
  --footer-text:#9a9a9a;
  --white:#fff;
}
*{box-sizing:border-box;margin:0;padding:0}
html,body{width:886px;height:1200px;overflow:hidden;background:var(--white)}
body{position:relative;font-family:'Roboto',sans-serif;color:var(--body)}
.abs{position:absolute}

/* top bar */
.topbar{left:0;top:0;width:886px;height:23px;border-bottom:1px solid #e6e6e6;background:#fafafa}
.contact-item{top:5px;font-size:8px;color:var(--ink);display:flex;align-items:center;gap:5px}
.social{right:148px;top:6px;display:flex;gap:7px}
.social span{width:10px;height:10px;border-radius:50%;background:#9c9c9c;display:block}

/* header */
.brand{left:142px;top:45px;display:flex;align-items:center;gap:6px}
.brand-dot{width:20px;height:20px;border-radius:50%;background:var(--blue)}
.brand-name{font-size:24px;font-weight:400;color:var(--blue);letter-spacing:-.3px}
.nav{left:348px;top:47px;display:flex;align-items:center;font-size:9.3px;color:var(--ink)}
.nav a{color:inherit;text-decoration:none;padding:5px 7px}
.nav a.active{background:var(--blue);color:var(--white);border-radius:2px;padding:5px 9px;margin:0 1px}

/* hero */
.hero{left:0;top:99px;width:886px;height:296px;overflow:hidden}
.hero-photo{position:absolute;inset:0;background:linear-gradient(90deg,#8c7b6c 0%,#b8a898 30%,#cfc3b6 55%,#a79383 75%,#6d6560 100%)}
.hero-person{position:absolute;left:540px;top:0;width:210px;height:296px;background:linear-gradient(180deg,#7a5c48,#5d5a5e 60%,#4b4a50);opacity:.55;border-radius:90px 90px 0 0}
.hero-title{left:142px;top:50px;font-size:88px;font-weight:700;color:var(--white);line-height:1;letter-spacing:-1px}
.hero-sub{left:141px;top:128px;font-size:23px;font-weight:300;color:var(--white);letter-spacing:-.2px}
.hero-points{left:142px;top:166px;list-style:none}
.hero-points li{display:flex;align-items:center;gap:7px;background:var(--blue);color:var(--white);font-size:11px;font-weight:500;height:15.5px;padding:0 8px 0 6px;margin-bottom:1px;width:max-content}
.dots{left:143px;top:251px;display:flex;gap:2px}
.dots span{width:10px;height:10px;border-radius:50%;background:var(--white);border:1px solid #ccc}
.dots span.on{background:var(--blue);border:2px solid var(--white)}

/* main */
.main-title{left:142px;top:416px;font-size:20.5px;font-weight:300;color:var(--ink)}
.copy{left:141px;width:402px;font-size:10.3px;line-height:16.4px;font-weight:300;color:var(--body)}
.benefit{left:142px;top:552px;width:372px;height:38px;background:linear-gradient(90deg,#e4e4e4 0%,#efefef 60%,rgba(255,255,255,0) 100%);display:flex;align-items:center}
.benefit-num{width:46px;height:38px;background:var(--blue);color:var(--white);font-size:27px;font-weight:700;display:flex;align-items:center;justify-content:center}
.benefit-text{font-size:14.5px;color:var(--ink);margin-left:6px;font-weight:400}
.benefits{left:142px;top:606px;list-style:none}
.benefits li{display:flex;align-items:center;gap:15px;font-size:8.6px;color:var(--ink);height:16.4px}
.callout{left:141px;top:937px;width:410px;font-size:10.4px;font-weight:500;color:#111;line-height:16.4px}
.callout em{font-style:normal;color:var(--red);font-weight:700}

/* sidebar */
.action{left:575px;width:155px;border:1px solid #d7d7d7;background:linear-gradient(#fdfdfd,#eee);display:flex;align-items:center;padding-left:12px;gap:13px}
.action b{display:block;font-size:11.5px;font-weight:500;color:#222;text-transform:uppercase}
.action span{display:block;font-size:11.5px;font-weight:300;color:#333}
.action.primary{background:linear-gradient(#1e8ccc,#0c609d);border-color:#0c609d}
.action.primary b,.action.primary span{color:var(--white)}
.promo{left:575px;top:609px;width:155px;height:134px;background:var(--red);color:var(--white);padding:14px 15px}
.promo h3{font-size:22.5px;font-weight:700;line-height:24px}
.promo p{font-size:10px;font-weight:300;line-height:14px;margin-top:12px}
.subscribe{left:575px;top:763px;width:156px;height:188px;border:1px solid #d7d7d7;padding:14px 14px 0 14px}
.subscribe h3{font-size:23px;font-weight:900;color:var(--blue);line-height:22px}
.subscribe h4{font-size:16px;font-weight:300;color:var(--blue);line-height:18px}
.subscribe p{font-size:9px;color:#555;line-height:14px;margin-top:4px}
.field{width:126px;height:22px;border:1px solid #ccc;margin-top:5px;display:flex;align-items:center;padding-left:8px;background:var(--white)}
.field:first-of-type{margin-top:11px}
.submit{width:126px;height:22px;margin-top:5px;background:linear-gradient(#23a3e0,#0f7cbf);color:var(--white);font-size:12px;font-weight:700;display:flex;align-items:center;justify-content:center}

/* footer */
.footer{left:0;top:1005px;width:886px;height:195px;background:var(--footer)}
.fcol{top:1033px}
.fcol h5{font-size:12.5px;font-weight:700;color:var(--blue);text-transform:uppercase;margin-bottom:9px}
.fcol li{list-style:none;font-size:8px;color:var(--footer-text);line-height:13.6px}
.visit li{display:flex;gap:8px;align-items:flex-start}
.copyright{left:0;top:1167px;width:886px;text-align:center;font-size:8px;color:var(--footer-text)}
</style>
</head>
<body>

<div class="abs topbar"></div>
<div class="abs contact-item" style="left:142px">
  <svg width="9" height="9" viewBox="0 0 10 10"><path d="M2 1l2 2-1 1.3c.6 1.2 1.5 2.1 2.7 2.7L7 6l2 2-1.3 1.3C4.5 9 1 5.5.7 2.3z" fill="#1b9ad6"/></svg>
  +9714-555-0182
</div>
<div class="abs contact-item" style="left:226px">
  <svg width="10" height="7" viewBox="0 0 10 7"><rect width="10" height="7" fill="#1b9ad6"/><path d="M0 0l5 4 5-4" stroke="#fff" fill="none" stroke-width=".8"/></svg>
  info@example.com
</div>
<div class="abs social"><span></span><span></span><span></span><span></span><span></span><span></span><span></span></div>

<div class="abs brand"><span class="brand-name">CEDAR VOICE</span><span class="brand-dot"></span></div>
<nav class="abs nav">
  <a>About Us</a><a class="active">Our Services</a><a>Our Methodology</a><a>FAQ</a><a>How it Works</a><a>Pricing</a><a>Contact Us</a>
</nav>

<section class="abs hero">
  <div class="hero-photo" role="img" aria-label="Blurred office background with a smiling receptionist wearing a headset, arms folded"></div>
  <div class="hero-person"></div>
</section>
<h1 class="abs hero-title" style="top:149px">24/7 LIVE</h1>
<p class="abs hero-sub" style="top:227px">RECEPTIONIST &amp; Answering Service</p>
<ul class="abs hero-points" style="top:265px">
  <li><svg width="10" height="10" viewBox="0 0 10 10"><rect x=".5" y="1.5" width="8" height="8" fill="none" stroke="#fff"/><path d="M2 5l2 2 5-6" stroke="#fff" fill="none" stroke-width="1.3"/></svg>US Based Receptionists</li>
  <li><svg width="10" height="10" viewBox="0 0 10 10"><rect x=".5" y="1.5" width="8" height="8" fill="none" stroke="#fff"/><path d="M2 5l2 2 5-6" stroke="#fff" fill="none" stroke-width="1.3"/></svg>Free trial, No credit card</li>
  <li><svg width="10" height="10" viewBox="0 0 10 10"><rect x=".5" y="1.5" width="8" height="8" fill="none" stroke="#fff"/><path d="M2 5l2 2 5-6" stroke="#fff" fill="none" stroke-width="1.3"/></svg>Affordable Prices</li>
  <li><svg width="10" height="10" viewBox="0 0 10 10"><rect x=".5" y="1.5" width="8" height="8" fill="none" stroke="#fff"/><path d="M2 5l2 2 5-6" stroke="#fff" fill="none" stroke-width="1.3"/></svg>Local or Toll Free Numbers Available</li>
</ul>
<div class="abs dots" style="top:350px"><span></span><span class="on"></span><span></span><span></span></div>

<h2 class="abs main-title">24/7 Live Receptionist &amp; Answering Service</h2>
<p class="abs copy" style="top:455px">Cedar Voice is a 24/7 call center and live answering service, we provide customized solutions for small, medium, and large organizations. Our customized solutions help our clients get the maximum return on their investment by capturing more leads and projecting a professional image to their customers, in addition to huge savings on overhead and labor costs.</p>

<div class="abs benefit"><div class="benefit-num">10</div><div class="benefit-text">Ways Your Company Can Benefit:</div></div>

<ul class="abs benefits">
  <li><svg width="10" height="10" viewBox="0 0 10 10"><rect x=".5" y="1.5" width="8" height="8" fill="none" stroke="#333"/><path d="M2 5l2 2 5-6" stroke="#333" fill="none" stroke-width="1.2"/></svg>Capture more business &amp; increase profits.</li>
  <li><svg width="10" height="10" viewBox="0 0 10 10"><rect x=".5" y="1.5" width="8" height="8" fill="none" stroke="#333"/><path d="M2 5l2 2 5-6" stroke="#333" fill="none" stroke-width="1.2"/></svg>Save thousands on labor costs.</li>
  <li><svg width="10" height="10" viewBox="0 0 10 10"><rect x=".5" y="1.5" width="8" height="8" fill="none" stroke="#333"/><path d="M2 5l2 2 5-6" stroke="#333" fill="none" stroke-width="1.2"/></svg>Improve your company's "phone image".</li>
  <li><svg width="10" height="10" viewBox="0 0 10 10"><rect x=".5" y="1.5" width="8" height="8" fill="none" stroke="#333"/><path d="M2 5l2 2 5-6" stroke="#333" fill="none" stroke-width="1.2"/></svg>Streamline your call flow.</li>
  <li><svg width="10" height="10" viewBox="0 0 10 10"><rect x=".5" y="1.5" width="8" height="8" fill="none" stroke="#333"/><path d="M2 5l2 2 5-6" stroke="#333" fill="none" stroke-width="1.2"/></svg>Conduct business 24/7 without the overhead.</li>
  <li><svg width="10" height="10" viewBox="0 0 10 10"><rect x=".5" y="1.5" width="8" height="8" fill="none" stroke="#333"/><path d="M2 5l2 2 5-6" stroke="#333" fill="none" stroke-width="1.2"/></svg>Take advantage of a turn-key, streamlined solution.</li>
  <li><svg width="10" height="10" viewBox="0 0 10 10"><rect x=".5" y="1.5" width="8" height="8" fill="none" stroke="#333"/><path d="M2 5l2 2 5-6" stroke="#333" fill="none" stroke-width="1.2"/></svg>Respond instantaneously to clients and prospects.</li>
  <li><svg width="10" height="10" viewBox="0 0 10 10"><rect x=".5" y="1.5" width="8" height="8" fill="none" stroke="#333"/><path d="M2 5l2 2 5-6" stroke="#333" fill="none" stroke-width="1.2"/></svg>Cedar Voice uses the most reliable equipment in the industry.</li>
  <li><svg width="10" height="10" viewBox="0 0 10 10"><rect x=".5" y="1.5" width="8" height="8" fill="none" stroke="#333"/><path d="M2 5l2 2 5-6" stroke="#333" fill="none" stroke-width="1.2"/></svg>Cedar Voice selects the right people with the best voices.</li>
  <li><svg width="10" height="10" viewBox="0 0 10 10"><rect x=".5" y="1.5" width="8" height="8" fill="none" stroke="#333"/><path d="M2 5l2 2 5-6" stroke="#333" fill="none" stroke-width="1.2"/></svg>Cedar Voice over-staffs receptionists to minimize hold times.</li>
</ul>

<p class="abs copy" style="top:789px">At Cedar Voice, we customize our services to each client's specific needs. We do not provide a "one size fits all" solutions. We take pride in developing solutions to fit the specific requirements of our clients' individual situation and needs.</p>
<p class="abs copy" style="top:855px">We employ the right people with the best voices and over-staff our team of live receptionists to minimize hold times. Our team of experts has experience spanning decades and cutting across industries to provide our customers with the right solution for their niche area of operation.</p>
<p class="abs callout">For more information or to speak with an account specialist, please call Cedar Voice at <em>+9714-555-0182!</em></p>

<!-- sidebar -->
<div class="abs action" style="top:421px;height:57px">
  <svg width="38" height="28" viewBox="0 0 38 28"><path d="M2 9h6l9-7v24l-9-7H2z" fill="#333"/><path d="M21 9q3 5 0 10M25 6q5 8 0 16M29 3q7 11 0 22" stroke="#333" stroke-width="2" fill="none"/></svg>
  <div><b>Listen to a</b><span>Live Demo</span></div>
</div>
<div class="abs action primary" style="top:481px;height:55px">
  <svg width="38" height="28" viewBox="0 0 38 28"><g fill="#fff"><rect x="12" y="3" width="24" height="3"/><rect x="12" y="8" width="24" height="3"/><rect x="12" y="13" width="24" height="3"/><rect x="12" y="18" width="24" height="3"/><rect x="12" y="23" width="24" height="3"/><circle cx="10" cy="17" r="9"/></g><text x="10" y="21.5" font-size="12" font-weight="700" text-anchor="middle" fill="#0c609d" font-family="Roboto,sans-serif">$</text></svg>
  <div><b>Request for</b><span>Pricing</span></div>
</div>
<div class="abs action" style="top:539px;height:56px">
  <svg width="38" height="30" viewBox="0 0 38 30"><rect x="12" y="6" width="16" height="23" rx="8" fill="#333"/><path d="M20 6v8M12 14h16" stroke="#eee" stroke-width="1.2"/><path d="M20 6C20 0 10 4 4 2" stroke="#333" stroke-width="1.5" fill="none"/></svg>
  <div><b>Free Online</b><span>Signup</span></div>
</div>
<div class="abs promo">
  <h3>24/7/365<br>LIVE DUBAI</h3>
  <p>Receptionist 100%<br>Satisfaction Guaranteed<br>NO Long-Term Contract</p>
</div>
<form class="abs subscribe">
  <h3>SUBSCRIBE</h3>
  <h4>Nesletter</h4>
  <p>Sign up for our FREE Monthly Newsletter</p>
  <div class="field"><svg width="11" height="11" viewBox="0 0 11 11"><circle cx="5.5" cy="3" r="2.6" fill="#aaa"/><path d="M0 11c0-4 2.5-5 5.5-5s5.5 1 5.5 5z" fill="#aaa"/></svg></div>
  <div class="field"><svg width="12" height="8" viewBox="0 0 12 8"><rect width="12" height="8" fill="#aaa"/><path d="M0 0l6 4.5L12 0" stroke="#fff" fill="none"/></svg></div>
  <div class="submit">SUBMIT</div>
</form>

<footer class="abs footer"></footer>
<div class="abs fcol" style="left:142px"><h5>Industries</h5><ul><li>Healthcare</li><li>Attorneys</li><li>Small Business</li><li>Service Professionals</li></ul></div>
<div class="abs fcol" style="left:282px"><h5>Services</h5><ul><li>24/7 Live Answering</li><li>Virtual Receptionist</li><li>Web Chat</li><li>Order Taking</li></ul></div>
<div class="abs fcol" style="left:429px"><h5>Phone Answering</h5><ul><li>24 Hour Answering Service</li><li>Incoming Call Management</li><li>Live Phone Answering</li><li>Toll-Free Answering Service</li></ul></div>
<div class="abs fcol visit" style="left:624px"><h5>Visit Us</h5><ul>
  <li><svg width="8" height="10" viewBox="0 0 8 10" style="margin-top:2px"><path d="M4 10L1 5a3.2 3.2 0 1 1 6 0z" fill="#9a9a9a"/><circle cx="4" cy="3.5" r="1.2" fill="#1b1b1b"/></svg><span>Cedar Voice P.O. Box 1207<br>Dubai, United Arab Emirates</span></li>
  <li style="margin-top:3px"><svg width="9" height="7" viewBox="0 0 9 7" style="margin-top:3px"><rect width="9" height="7" fill="#9a9a9a"/><path d="M0 0l4.5 3.5L9 0" stroke="#1b1b1b" fill="none" stroke-width=".8"/></svg><span>info@cedarvoice.net</span></li>
</ul></div>
<p class="abs copyright">Copyright © 2013. All Rights Reserved &nbsp;|&nbsp; Privacy Policy &nbsp;|&nbsp; Terms and Conditions</p>

</body>
</html>
```